Creative - Appealing - Business Card Design Project

Looking for a Business card design (vector artwork) for an existing company called 'Fernway Sound'. We operate in the entertainment industry specializing in audio system design and rental, however; we also deal with other sectors of the entertainment industry including lighting, video, staging and power system design and rental. We would like to see designs that don't focus too much on audio but include elements encompassing everything else.

Double sided business card, following our new colour scheme and logo, which is attached. The card would ideally be creative and eye catching to draw in new customers in the elegant event production market, such as weddings & corporate affairs.

Target Market(s)

High end corporate clients, wedding clients

Industry/Entity Type

Entertainment

Requirements
Must have
• Our contact details, these can be worded & listed however you think appropriate as part as the design

Business Name - Fernway Sound
My Name - Dominic Harwell
Web Address - www.fernwaysound-example.com
Mobile Number - 07914 362 517
Office Number - 0330 481 7265
Email - dom@fernwaysound-example.com

The name, email and mobile number would need to be able to be changed to my business partners also.

The font used on our logo is Sansation
Nice to have
• On one side maybe a word cloud involving the services in which we can provide; Lighting, Sound, Event Production, Staging, LED Uplighting, Projection Mapping, Wedding Hire

On the other side, all the important credentials of contact.
Should not have
• The design should not use any old style fonts (i.e Times New Roman, Gothic etc) or on the other side of the scale, any 'jokey' fonts (i.e. Comic Sans).

The font to be used is Sansation

```html
<!DOCTYPE html>
<html lang="en">
<head>
<meta charset="utf-8">
<title>Fernway Sound – Business Card</title>
<link rel="stylesheet" href="https://fonts.googleapis.com/css2?family=Exo+2:wght@300;400;700&display=swap">
<style>
  :root {
    --purple: #5b3a93;
    --purple-light: #6c4aa8;
    --purple-dark: #3f2471;
    --grey: #8a8a8a;
    --grey-light: #b4b4b4;
    --card-white: #f7f7f7;
    --ink: #6a6a6a;
    --backdrop: #3a3a3a;
  }
  * { margin: 0; padding: 0; box-sizing: border-box; }
  html, body {
    width: 1200px; height: 900px; overflow: hidden;
    background: var(--backdrop);
    font-family: "Exo 2", sans-serif;
  }
  .sheet {
    width: 1200px; height: 900px;
    display: flex; flex-direction: column;
    align-items: center; justify-content: center; gap: 56px;
  }
  .card {
    position: relative;
    width: 640px; height: 366px;
    overflow: hidden;
    box-shadow: 0 10px 30px rgba(0,0,0,.45);
  }

  /* Back side */
  .card--back {
    background: linear-gradient(135deg, var(--purple-dark) 0%, var(--purple) 55%, var(--purple-light) 100%);
  }
  .card--back .wordmark {
    position: absolute; right: 90px; top: 130px;
    color: #fff; font-weight: 700; font-size: 40px;
    letter-spacing: 1px; text-transform: uppercase; line-height: 1.1;
    text-align: right; white-space: nowrap;
  }
  .wordmark span { display: block; }

  /* Front side */
  .card--front { background: var(--card-white); }
  .brand { position: absolute; left: 52px; top: 78px; width: 250px; }
  .brand__square {
    width: 54px; height: 54px; background: var(--purple);
    margin-left: 74px; margin-bottom: 16px;
  }
  .brand__name {
    color: var(--grey); font-weight: 700; font-size: 32px;
    text-transform: uppercase; line-height: 1.05; letter-spacing: .5px;
    white-space: nowrap;
  }
  .brand__name span { display: block; }
  .holder {
    position: absolute; left: 338px; top: 72px;
    color: var(--purple); font-weight: 400; font-size: 21px; white-space: nowrap;
  }
  .contacts { position: absolute; left: 350px; top: 128px; list-style: none; }
  .contacts li {
    display: flex; align-items: center; gap: 12px; white-space: nowrap;
    color: var(--ink); font-weight: 300; font-size: 15px; height: 24px;
  }
  .contacts svg { width: 17px; height: 17px; flex: none; }
  .rule { position: absolute; background: var(--grey-light); height: 5px; }
  .rule--upper { left: 628px; right: 0; top: 218px; }
  .rule--middle { left: 28px; width: 336px; top: 262px; }
  .rule--bottom { left: 28px; right: 0; top: 334px; }
  .web {
    position: absolute; left: 354px; top: 244px; width: 274px; height: 34px;
    background: var(--purple); color: #fff;
    font-weight: 300; font-size: 15px; white-space: nowrap;
    display: flex; align-items: center; justify-content: center;
  }
</style>
</head>
<body>
<main class="sheet">

  <section class="card card--back" aria-label="Card back">
    <div class="wordmark"><span>Fernway</span><span>Sound</span></div>
  </section>

  <section class="card card--front" aria-label="Card front">
    <div class="brand">
      <div class="brand__square"></div>
      <div class="brand__name"><span>Fernway</span><span>Sound</span></div>
    </div>

    <div class="holder">Dominic Harwell</div>

    <ul class="contacts">
      <li>
        <svg viewBox="0 0 20 20" aria-hidden="true"><circle cx="10" cy="10" r="10" fill="#5b3a93"/><rect x="7" y="4.5" width="6" height="11" rx="1" fill="none" stroke="#fff" stroke-width="1.3"/><circle cx="10" cy="13.3" r=".8" fill="#fff"/></svg>
        07914 362 517
      </li>
      <li>
        <svg viewBox="0 0 20 20" aria-hidden="true"><circle cx="10" cy="10" r="10" fill="#5b3a93"/><path d="M5 8 Q10 4 15 8 L13.5 9.5 L12 8.5 L8 8.5 L6.5 9.5 Z" fill="#fff"/><rect x="6.5" y="10" width="7" height="4.5" rx="1" fill="#fff"/></svg>
        0330 481 7265
      </li>
      <li>
        <svg viewBox="0 0 20 20" aria-hidden="true"><circle cx="10" cy="10" r="10" fill="#5b3a93"/><text x="10" y="13.8" text-anchor="middle" font-size="11" font-family="Exo 2, sans-serif" fill="#fff">@</text></svg>
        dom@fernwaysound-example.com
      </li>
    </ul>

    <div class="rule rule--upper"></div>
    <div class="rule rule--middle"></div>
    <div class="web">www.fernwaysound-example.com</div>
    <div class="rule rule--bottom"></div>
  </section>

</main>
</body>
</html>
```